Landing page for a sports website

we have a sports tracking and management website and require a web site.
the site should have the ability to have 2 options for selection the first being a competitions portal the other a club portal there should be a about us page and a contact us page
the site should be dynamic and vibrant and be easily recognisable as a multiple sports page
we also have www.tilvoshelf.net and would like it to compliment that site
i would like to have some form of animation regarding sports occur when you click the login option if that is possible
the site is www.drqplays.net and I have attached the logo in both 3d and standard
we also require a design several templates for information pages please see www.lunaforge.net as an example of how it should look but with a sports theme
Target Market(s)
This will be used for primarily team based sports
Industry/Entity Type
Management
Number of Pages Required
3 page
Requirements
Must have
- the ability to change the logo and names of the site
- i.e. from drqplays to drqcampus at a later date

```html
<!DOCTYPE html>
<html lang="en">
<head>
<meta charset="utf-8">
<title>DRQ Plays — Sports Management</title>
<link href="https://fonts.googleapis.com/css2?family=Open+Sans:wght@400;600;700&display=swap" rel="stylesheet">
<style>
:root{
  --red:#d9362b;
  --red-dark:#b8261d;
  --blue:#1ea7e1;
  --blue-dark:#0d8cc9;
  --orange:#ec7a1c;
  --ink:#333;
  --grey-bg:#ececec;
  --field:#e9e9e9;
  --dark-btn:#2b2b2b;
  --footer:#0f3f8c;
  --white:#fff;
}
*{box-sizing:border-box;margin:0;padding:0}
html,body{width:1200px;height:2578px;overflow:hidden}
body{font-family:"Open Sans",Arial,sans-serif;color:var(--ink);position:relative;background:#fff}
.abs{position:absolute}

/* hero */
.hero{position:absolute;left:0;top:0;width:1200px;height:630px;
  background:linear-gradient(180deg,#8fb6dc 0%,#b9cfe0 30%,#7e8a78 55%,#6b6e5e 75%,#8a8a84 100%)}
.hero-photo{position:absolute;inset:0}
.brand{left:86px;top:34px;height:110px;display:flex;align-items:center;gap:14px;white-space:nowrap;
  font-weight:700;font-size:52px;color:var(--blue-dark);letter-spacing:1px}
.brand-dot{width:30px;height:30px;border-radius:50%;background:var(--red);flex:none}
.main-nav{left:716px;top:34px;width:474px;height:46px;background:var(--red);
  clip-path:polygon(0 0,100% 0,100% 100%,6% 100%);display:flex;align-items:center;justify-content:flex-end;
  padding-right:40px;gap:22px;color:#fff;font-size:16px;white-space:nowrap}
.main-nav span.sep{opacity:.8}
.social{top:86px;display:flex;gap:20px;left:888px}
.social i{width:62px;height:62px;border-radius:50%;background:#fff;display:block}
.hero-title{top:292px;left:0;width:1200px;text-align:center;color:#fff;font-weight:700;font-size:54px;line-height:66px;
  text-shadow:0 2px 6px rgba(0,0,0,.35)}
.hero-sub{top:356px;left:0;width:1200px;text-align:center;color:#fff;font-size:38px;line-height:48px;
  text-shadow:0 2px 6px rgba(0,0,0,.35)}
.portal{top:435px;height:52px;border-radius:6px;color:#fff;font-weight:700;font-size:17px;
  display:flex;align-items:center;justify-content:center;text-transform:uppercase;white-space:nowrap}
.portal.comp{left:335px;width:246px;background:linear-gradient(#3cc0f0,var(--blue-dark));border-bottom:4px solid #0a6fa3}
.portal.club{left:604px;width:255px;background:linear-gradient(#f59a3c,#dc6a10);border-bottom:4px solid #a94f0a}
.slide-arrow{top:338px;width:40px;height:40px;border-radius:50%;background:var(--orange)}

/* welcome */
.welcome{position:absolute;top:630px;left:0;width:1200px;height:344px;
  background:linear-gradient(135deg,#f1f1f1,#e3e3e3 50%,#efefef)}
.welcome h1{position:absolute;top:40px;width:1200px;text-align:center;font-size:44px;font-weight:600;color:var(--blue-dark)}
.welcome h1 b{color:var(--red);font-weight:700}
.welcome p{position:absolute;top:112px;left:90px;width:1020px;text-align:center;font-size:14px;line-height:24px;color:#444}
.btn-dark{position:absolute;background:var(--dark-btn);color:#fff;font-size:20px;display:flex;align-items:center;justify-content:center;border-radius:2px}
.welcome .btn-dark{top:246px;left:518px;width:175px;height:49px}

/* why */
.why{position:absolute;top:974px;left:0;width:1200px;height:449px;background:#fff}
.why-icon{position:absolute;left:100px;top:55px;width:46px;height:46px;border-radius:50%;background:var(--orange)}
.why h2{position:absolute;left:170px;top:54px;font-size:34px;font-weight:600;color:#222;letter-spacing:.5px;white-space:nowrap}
.why-photo{position:absolute;left:100px;top:143px;width:222px;height:222px;border-radius:50%;
  background:radial-gradient(circle at 50% 40%,#d8d8d8,#8d9a86 60%,#5f6b57)}
.features{position:absolute;top:124px;list-style:none}
.features li{height:47px;display:flex;align-items:center;gap:16px;font-size:20px;color:#444;white-space:nowrap}
.features li svg{flex:none}
.f1{left:504px}.f2{left:819px}

/* testimonial */
.testimonial{position:absolute;top:1423px;left:0;width:1200px;height:476px;
  background:linear-gradient(180deg,#2eb1e8,#10a0dd 60%,#0b97d6)}
.avatar{position:absolute;border-radius:50%;border:6px solid #fff;background:linear-gradient(#e4d5c8,#b7a393)}
.testimonial h3{position:absolute;top:312px;width:1200px;text-align:center;color:#fff;font-size:20px;font-weight:700}
.testimonial blockquote{position:absolute;top:360px;left:150px;width:900px;text-align:center;color:#fff;font-size:15px;line-height:22px}

/* contact */
.contact{position:absolute;top:1899px;left:0;width:1200px;height:558px;background:#fff}
.contact h2{position:absolute;top:52px;width:1200px;text-align:center;color:var(--red);font-size:30px;font-weight:600;letter-spacing:1px}
.c-line{position:absolute;left:0;width:1200px;display:flex;justify-content:center;align-items:center;gap:14px;font-size:16px;color:#444}
.field{position:absolute;background:var(--field);border:1px solid #ddd;font-size:15px;color:#333;padding:8px 12px}
.contact .btn-dark{top:449px;left:518px;width:175px;height:49px}

/* footer */
.site-footer{position:absolute;top:2457px;left:0;width:1200px;height:121px;
  background:linear-gradient(90deg,#0c2f6e,#1550a6 50%,#0c336f)}
.foot-nav{position:absolute;left:96px;top:28px;color:#fff;font-size:15px;display:flex;gap:28px}
.foot-brand{position:absolute;left:96px;top:64px;color:#fff;font-weight:700;font-size:24px;line-height:32px;white-space:nowrap}
.foot-copy{position:absolute;left:242px;top:72px;color:#fff;font-size:14px;line-height:20px;white-space:nowrap}
.foot-social{position:absolute;left:985px;top:42px;display:flex;gap:14px}
.foot-social i{width:32px;height:32px;border-radius:50%;background:#fff;display:block}
</style>
</head>
<body>

<header class="hero">
  <div class="hero-photo" role="img" aria-label="Cyclist in a yellow jersey riding a racing bike on an open mountain road"></div>
  <div class="abs brand"><span class="brand-dot"></span>DRQ Plays</div>
  <nav class="abs main-nav"><span>HOME</span><span class="sep">//</span><span>ABOUT US</span><span class="sep">//</span><span>CONTACT US</span></nav>
  <div class="abs social"><i></i><i></i><i></i></div>
  <div class="abs hero-title">Lorem Ipsum is simply dummy</div>
  <div class="abs hero-sub">of the printing and typesetting industry</div>
  <a class="abs portal comp">Competitions Portal</a>
  <a class="abs portal club">Club Portal</a>
  <div class="abs slide-arrow" style="left:52px"><svg width="40" height="40"><path d="M23 13l-7 7 7 7" fill="none" stroke="#fff" stroke-width="3"/></svg></div>
  <div class="abs slide-arrow" style="left:1106px"><svg width="40" height="40"><path d="M17 13l7 7-7 7" fill="none" stroke="#fff" stroke-width="3"/></svg></div>
</header>

<section class="welcome">
  <h1>Welcome <b>DRQ Plays</b></h1>
  <p>Lorem ipsum dolor sit amet conse ctetur adipisicing elit, sed do eiusmod tempor incididunt ut labore et dolore magna aliqua. Ut enim ad minim veniam, quis nostrud exercitation ullamco laboris nisi ut aliquip ex ea commodo consequat. Duis aute irure dolor in reprehenderit in voluptate velit esse cillum dolore eu fugiat nulla pariatur. Lorem ipsum dolor sit amet conse ctetur adipisicing elit, sed do eiusmod tempor incididunt ut labore et dolore magna aliqua. Ut enim ad minim veniam, quis nostrud exercitation ullamco laboris.</p>
  <a class="btn-dark">Read more</a>
</section>

<section class="why">
  <div class="why-icon"></div>
  <h2>WHY CHOOSE DRQ PLAYS</h2>
  <div class="why-photo" role="img" aria-label="Red and black rally car on a track"></div>
  <svg class="abs" style="left:318px;top:120px" width="110" height="90"><path d="M4 84 Q40 20 100 10" fill="none" stroke="var(--blue)" stroke-width="3"/><path d="M86 4l16 6-12 12" fill="none" stroke="var(--blue)" stroke-width="3"/></svg>
  <ul class="features f1">
    <li><svg width="26" height="26"><circle cx="13" cy="13" r="13" fill="var(--blue)"/><path d="M7 13l4 4 8-8" fill="none" stroke="#fff" stroke-width="3"/></svg>Lorem Ipsum</li>
    <li><svg width="26" height="26"><circle cx="13" cy="13" r="13" fill="var(--blue)"/><path d="M7 13l4 4 8-8" fill="none" stroke="#fff" stroke-width="3"/></svg>Contrary to popular</li>
    <li><svg width="26" height="26"><circle cx="13" cy="13" r="13" fill="var(--blue)"/><path d="M7 13l4 4 8-8" fill="none" stroke="#fff" stroke-width="3"/></svg>Typesetting</li>
    <li><svg width="26" height="26"><circle cx="13" cy="13" r="13" fill="var(--blue)"/><path d="M7 13l4 4 8-8" fill="none" stroke="#fff" stroke-width="3"/></svg>Established</li>
    <li><svg width="26" height="26"><circle cx="13" cy="13" r="13" fill="var(--blue)"/><path d="M7 13l4 4 8-8" fill="none" stroke="#fff" stroke-width="3"/></svg>Opposed</li>
    <li><svg width="26" height="26"><circle cx="13" cy="13" r="13" fill="var(--blue)"/><path d="M7 13l4 4 8-8" fill="none" stroke="#fff" stroke-width="3"/></svg>Contrary to popular</li>
  </ul>
  <ul class="features f2">
    <li><svg width="26" height="26"><circle cx="13" cy="13" r="13" fill="var(--blue)"/><path d="M7 13l4 4 8-8" fill="none" stroke="#fff" stroke-width="3"/></svg>Sometimes</li>
    <li><svg width="26" height="26"><circle cx="13" cy="13" r="13" fill="var(--blue)"/><path d="M7 13l4 4 8-8" fill="none" stroke="#fff" stroke-width="3"/></svg>Sometimes by Accident</li>
    <li><svg width="26" height="26"><circle cx="13" cy="13" r="13" fill="var(--blue)"/><path d="M7 13l4 4 8-8" fill="none" stroke="#fff" stroke-width="3"/></svg>Randomised</li>
    <li><svg width="26" height="26"><circle cx="13" cy="13" r="13" fill="var(--blue)"/><path d="M7 13l4 4 8-8" fill="none" stroke="#fff" stroke-width="3"/></svg>Translation</li>
    <li><svg width="26" height="26"><circle cx="13" cy="13" r="13" fill="var(--blue)"/><path d="M7 13l4 4 8-8" fill="none" stroke="#fff" stroke-width="3"/></svg>Reasonable</li>
  </ul>
</section>

<section class="testimonial">
  <div class="avatar" style="left:189px;top:126px;width:123px;height:123px" role="img" aria-label="Client portrait"></div>
  <div class="avatar" style="left:329px;top:126px;width:123px;height:123px" role="img" aria-label="Client portrait"></div>
  <div class="avatar" style="left:495px;top:81px;width:207px;height:207px" role="img" aria-label="Featured client portrait"></div>
  <div class="avatar" style="left:750px;top:126px;width:123px;height:123px" role="img" aria-label="Client portrait"></div>
  <div class="avatar" style="left:890px;top:126px;width:123px;height:123px" role="img" aria-label="Client portrait"></div>
  <h3>R. CALDER, UTAH</h3>
  <blockquote>"This company is amazing!! We have worked with them for about four weeks now. When I say worked,<br>I mean, gave them info and sat back and watched. Thank you ClearLedger.com for making this process so stress free!!"</blockquote>
</section>

<section class="contact">
  <h2>CONTACT US</h2>
  <div class="c-line" style="top:104px"><svg width="18" height="26"><path d="M9 25C3 16 1 12 1 9a8 8 0 0 1 16 0c0 3-2 7-8 16z" fill="var(--orange)"/><circle cx="9" cy="9" r="3" fill="#fff"/></svg>Address goes here, city name Pin code , countryname</div>
  <div class="c-line" style="top:142px"><svg width="24" height="18"><rect width="24" height="18" rx="2" fill="var(--orange)"/><path d="M1 2l11 8 11-8" fill="none" stroke="#fff" stroke-width="2"/></svg>info@drqplays.net</div>
  <div class="c-line" style="top:180px"><svg width="16" height="28"><rect width="16" height="28" rx="3" fill="var(--orange)"/><rect x="3" y="4" width="10" height="16" fill="#fff"/></svg>(123) 456-7890</div>
  <div class="field" style="left:246px;top:232px;width:344px;height:37px">Name</div>
  <div class="field" style="left:604px;top:232px;width:344px;height:37px">Email Address</div>
  <div class="field" style="left:246px;top:278px;width:344px;height:37px">Phone Number</div>
  <div class="field" style="left:604px;top:278px;width:344px;height:37px">Sebject</div>
  <div class="field" style="left:246px;top:321px;width:702px;height:108px">Massage</div>
  <a class="btn-dark">Send</a>
</section>

<footer class="site-footer">
  <nav class="foot-nav"><span>Home</span><span>|</span><span>About Us</span><span>|</span><span>Contact Us</span></nav>
  <div class="foot-brand">DRQ Plays</div>
  <div class="foot-copy">Copyright © 2015 Fennick Studio</div>
  <div class="foot-social"><i></i><i></i><i></i></div>
</footer>

</body>
</html>
```